Liquor Label / Aguardiente

Label design for liquor bottle. Designers may submit multiple submissions.

Product Description:
Name: Viento de Plata™
Alcohol Category: Aguardiente (which in Spanish most closely translates to “burning water”) – aguardiente is derived from
cane sugar and is a general term for a type of alcoholic spirit in many Central and South America countries.
Taste: A smooth liquor with a comfortable yet spicy finish
Smell: Subtle aroma of spicy jalapeños
Liquid Color: Clear
Bottle Color: Clear
See link for reference - http://www.kelvostamp.com/sites/default/files/styles/uc_product_full/public/Pemrow_0.jpg?itok=9QmT2xLp
Closure: Bar top / cork
Bottle Shape/Size: height = 8.67in; diameter of base = 3.70in; diameter of neck = 0.85in

Label may consist of two separate parts (i.e. front and back, front and vertical side), or one continuous label.

Designer has complete freedom with color, font etc. unless otherwise stated below. The label MUST
contain (but is not limited only to) the following text exactly as written in quotes below:
- “Viento de Plata”
- “Aguardiente”
- “Cane Neutral Spirit with Natural Flavors”
- “35% Alc./Vol.”
- “750 ml”
- “Bottled by WP Spirits, LLC” and “Nashville, TN” - “Government Warning: (1) According to the Surgeon General, women should not drink alcoholic beverages during
pregnancy because of the risk of birth defects. (2) Consumption of alcoholic beverages impairs your ability to
drive a car or operate machinery, and may cause health problems.” (text in previous quotes must be in all
capitalized letters, text must be 2 MM in height and quote must be separated 2MM by all other text)
- Must be dedicated empty space for bar code (approximately 0.75in. height x 1.25in. length)

Target Market(s)

Label should have mass market appeal.
Age: 21 – 28 years old (primary target market is 21+ year old college students and recent graduates)
Target Market Gender: Both male and female, with emphasis on male
Consumption Focus: Spirit will be consumed typically as a shot, primarily at bars and secondarily off premise (label design will be critical for making our product highly visible behind a bar)
Marketing Theme: South American elements. The official Viento de Plata mascot is a llama and the incorporation and use of a llama somewhere (however large or small) on the bottle is encourage but by no means required.

Industry/Entity Type

Health

Requirements
Should not have
• Elements that may lead a potential consumer to believe the beverage is a craft liquor or an artisan brand. Please do not include images of peppers.

```html
<!DOCTYPE html>
<html lang="en">
<head>
<meta charset="utf-8">
<title>Viento de Plata – Aguardiente Label</title>
<link rel="stylesheet" href="https://fonts.googleapis.com/css2?family=Fredoka:wght@600&family=Pinyon+Script&family=Pirata+One&family=Old+Standard+TT&display=swap">
<style>
  :root {
    --page: #ffffff;
    --mint: #9fd0c0;
    --mint-deep: #7fbcaa;
    --cream: #f4e7d7;
    --ink: #1e3833;
    --flame: #e2361c;
    --flame-soft: #f08a5a;
    --sketch: #cfc3b4;
  }
  * { margin: 0; padding: 0; box-sizing: border-box; }
  html, body {
    width: 1200px; height: 905px; overflow: hidden;
    background: var(--page);
  }
  .stage { position: relative; width: 1200px; height: 905px; }
  .label {
    position: absolute; left: 295px; top: 52px;
    width: 610px; height: 800px;
  }
  .label-frame { position: absolute; inset: 0; }
  .label-art {
    position: absolute; left: 34px; top: 34px; right: 34px; bottom: 58px;
    background:
      radial-gradient(ellipse 34% 26% at 52% 54%, var(--flame) 0%, var(--flame-soft) 55%, rgba(240,138,90,0) 100%),
      linear-gradient(180deg, var(--cream) 0%, #efe1cf 60%, var(--sketch) 100%);
  }
  .brand-name {
    position: absolute; left: 0; right: 0; top: 110px;
    text-align: center;
    font-family: "Fredoka", sans-serif; font-weight: 600;
    font-size: 54px; line-height: 1;
    color: var(--ink);
    letter-spacing: 1px;
    white-space: nowrap;
  }
  .category {
    position: absolute; left: 0; right: 0; top: 210px;
    text-align: center;
    font-family: "Pinyon Script", cursive;
    font-size: 54px; line-height: 1;
    color: var(--ink);
  }
  .specs {
    position: absolute; left: 420px; top: 685px;
    font-family: "Old Standard TT", serif;
    color: var(--flame);
    text-align: center;
    line-height: 1.2;
  }
  .specs .abv { font-size: 17px; }
  .specs .volume { font-size: 22px; }
  .descriptor {
    position: absolute; left: 0; right: 0; bottom: 18px;
    text-align: center;
    font-family: "Pirata One", cursive;
    font-size: 24px;
    color: var(--ink);
    letter-spacing: 0.5px;
  }
</style>
</head>
<body>
<main class="stage">
  <section class="label">
    <svg class="label-frame" width="610" height="800" viewBox="0 0 610 800" aria-hidden="true">
      <rect width="610" height="800" fill="var(--mint)"/>
      <rect x="6" y="6" width="598" height="788" fill="none" stroke="var(--mint-deep)" stroke-width="2"/>
      <rect x="30" y="30" width="550" height="716" fill="var(--cream)"/>
      <g fill="var(--cream)">
        <circle cx="30" cy="60" r="12"/><circle cx="30" cy="120" r="12"/><circle cx="30" cy="180" r="12"/>
        <circle cx="30" cy="240" r="12"/><circle cx="30" cy="300" r="12"/><circle cx="30" cy="360" r="12"/>
        <circle cx="30" cy="420" r="12"/><circle cx="30" cy="480" r="12"/><circle cx="30" cy="540" r="12"/>
        <circle cx="30" cy="600" r="12"/><circle cx="30" cy="660" r="12"/><circle cx="30" cy="720" r="12"/>
        <circle cx="580" cy="60" r="12"/><circle cx="580" cy="120" r="12"/><circle cx="580" cy="180" r="12"/>
        <circle cx="580" cy="240" r="12"/><circle cx="580" cy="300" r="12"/><circle cx="580" cy="360" r="12"/>
        <circle cx="580" cy="420" r="12"/><circle cx="580" cy="480" r="12"/><circle cx="580" cy="540" r="12"/>
        <circle cx="580" cy="600" r="12"/><circle cx="580" cy="660" r="12"/><circle cx="580" cy="720" r="12"/>
        <circle cx="70" cy="30" r="12"/><circle cx="130" cy="30" r="12"/><circle cx="190" cy="30" r="12"/>
        <circle cx="250" cy="30" r="12"/><circle cx="310" cy="30" r="12"/><circle cx="370" cy="30" r="12"/>
        <circle cx="430" cy="30" r="12"/><circle cx="490" cy="30" r="12"/><circle cx="550" cy="30" r="12"/>
      </g>
    </svg>
    <div class="label-art" role="img" aria-label="Sketched street scene with a struck match and a large red flame"></div>
    <h1 class="brand-name">VIENTO DE PLATA</h1>
    <p class="category">Aguardiente</p>
    <div class="specs">
      <p class="abv">35% Alc./Vol.</p>
      <p class="volume">750 ML.</p>
    </div>
    <p class="descriptor">Cane Neutral Spirit with Natural Flavors</p>
  </section>
</main>
</body>
</html>
```